Web Design Project

We are re-starting this project.

This project is for a totally new look and design of a website for Wablor. www.wablor-demo.net.

Wablor is a naming protocol for physical locations and can be used for fixed and mobile people, places and things. Find your friends, or find a business. Because Wablor locations point to precise geo-physical (GPS) co-ordinates, navigation to a location becomes totally reliable.
Updates

Please see the modified brief for this project

Target Market(s)

Every person and every business can have multiple !Wabs (Wablor locations), so the website needs to be appealing and fun, but easy to use and functional

Industry/Entity Type

Business

Colors
34a6d7

Requirements
Must have
• Uniqueness!

```html
<!DOCTYPE html>
<html lang="en">
<head>
<meta charset="utf-8">
<title>Wablor – Find people, places and things</title>
<link rel="stylesheet" href="https://fonts.googleapis.com/css2?family=Open+Sans:wght@300;400;600;700;800&display=swap">
<style>
  :root {
    --brand-blue: #34a6d7;
    --band-blue: rgba(30, 126, 180, 0.9);
    --text-dark: #333333;
    --text-muted: #6b6b6b;
    --divider: #bdbdbd;
    --action-green: #2bd67b;
    --action-green-dark: #1fae61;
    --store-dark: #222222;
    --store-light: #eeeeee;
    --white: #ffffff;
    --social-one: #3b5998;
    --social-two: #33a8e2;
  }
  * { box-sizing: border-box; margin: 0; padding: 0; }
  html, body { width: 1200px; height: 960px; overflow: hidden; background: var(--white); }
  body { font-family: "Open Sans", Arial, sans-serif; color: var(--text-dark); position: relative; }
  a { text-decoration: none; }

  .site-header { position: absolute; left: 0; top: 0; width: 1200px; height: 112px; }
  .brand { position: absolute; left: 100px; top: 22px; display: flex; align-items: center; gap: 10px;
    font-weight: 800; font-size: 50px; color: var(--brand-blue); letter-spacing: -1px; line-height: 1; }
  .brand-dot { width: 40px; height: 40px; border-radius: 50%; background: var(--brand-blue); }
  .account-nav { position: absolute; right: 99px; top: 44px; font-size: 13px; letter-spacing: .3px; }
  .account-nav .signup { color: var(--brand-blue); }
  .account-nav .login { color: var(--text-dark); }
  .account-nav .sep { color: var(--divider); margin: 0 9px; }

  .hero { position: absolute; left: 0; top: 112px; width: 1200px; height: 689px; overflow: hidden; }
  .hero-city { position: absolute; inset: 0;
    background:
      radial-gradient(ellipse 520px 260px at 300px 60px, rgba(235,244,246,.85), rgba(235,244,246,0) 70%),
      radial-gradient(ellipse 420px 300px at 80px 560px, rgba(120,82,52,.55), rgba(120,82,52,0) 70%),
      radial-gradient(ellipse 420px 360px at 1020px 520px, rgba(58,78,92,.55), rgba(58,78,92,0) 70%),
      radial-gradient(ellipse 300px 260px at 640px 540px, rgba(210,214,212,.45), rgba(210,214,212,0) 70%),
      linear-gradient(180deg, #e6eef0 0%, #e1e5e1 22%, #cfd2cb 38%, #a7aba7 50%, #7f8485 62%, #5d6164 76%, #4a4743 100%); }
  .hero-title { position: absolute; left: 0; top: 62px; width: 1200px; text-align: center;
    font-weight: 300; font-size: 39px; color: #555555; }
  .device { position: absolute; left: 155px; top: 173px; width: 241px; height: 490px; border-radius: 38px; z-index: 2;
    border: 1px solid #c9c9c9;
    background:
      linear-gradient(135deg, #efe9d6 0%, #e3e6d4 35%, #cfe0b8 60%, #eae5d2 100%) 12px 74px / 217px 327px no-repeat,
      linear-gradient(160deg, #f7f7f7 0%, #e4e4e4 100%);
    box-shadow: 0 8px 16px rgba(0,0,0,.3); }

  .search-band { position: absolute; left: 0; top: 591px; width: 1200px; height: 98px; background: var(--band-blue); }
  .search-prompt { position: absolute; left: 444px; top: 14px; font-weight: 700; font-size: 25px;
    line-height: 31px; color: var(--white); }
  .search-input { position: absolute; left: 654px; top: 25px; width: 310px; height: 47px;
    background: var(--white); font-size: 16px; color: #999999; padding-left: 17px; display: flex; align-items: center; }
  .search-button { position: absolute; left: 968px; top: 25px; width: 97px; height: 47px; border-radius: 2px;
    background: var(--action-green); border-bottom: 2px solid var(--action-green-dark);
    font-weight: 600; font-size: 17px; color: #184d33; display: flex; align-items: center; justify-content: center; }

  .feedback-tab { position: absolute; right: 0; top: 415px; width: 44px; height: 129px; z-index: 3;
    background: var(--action-green); border-radius: 4px 0 0 4px; display: flex; align-items: center; justify-content: center; }
  .feedback-tab span { transform: rotate(-90deg); font-weight: 600; font-size: 15px; color: #155a33; letter-spacing: 1px; white-space: nowrap; }

  .site-footer { position: absolute; left: 0; top: 801px; width: 1200px; height: 159px; }
  .footer-links { position: absolute; left: 101px; top: 31px; display: flex; font-size: 13.5px; color: var(--text-muted); }
  .footer-links a { color: var(--text-muted); }
  .footer-links .sep { color: var(--divider); margin: 0 12px; }
  .copyright { position: absolute; left: 101px; top: 62px; font-size: 13.5px; color: var(--text-muted); word-spacing: 2px; }
  .social { position: absolute; left: 100px; top: 96px; display: flex; gap: 8px; }
  .social-dot { width: 34px; height: 34px; border-radius: 50%; }
  .social-dot.one { background: var(--social-one); }
  .social-dot.two { background: var(--social-two); }
  .download-label { position: absolute; left: 690px; top: 31px; font-size: 13.5px; color: var(--text-muted); }
  .store { position: absolute; top: 64px; width: 201px; height: 66px; display: flex; align-items: center; gap: 14px; padding-left: 26px; border-radius: 2px; }
  .store.market { left: 690px; background: var(--store-dark); color: var(--white); }
  .store.shelf { left: 899px; background: var(--store-light); color: var(--text-dark); }
  .store-icon { width: 30px; height: 30px; border-radius: 50%; flex: none; }
  .market .store-icon { background: #dddddd; }
  .shelf .store-icon { background: #7fb8d8; }
  .store-text { font-size: 12.5px; line-height: 18px; letter-spacing: -.3px; }
  .store-text strong { display: block; font-weight: 600; font-size: 14px; }
</style>
</head>
<body>
  <header class="site-header">
    <div class="brand"><span class="brand-dot"></span>Wablor</div>
    <nav class="account-nav">
      <a class="signup" href="#">SIGN UP</a><span class="sep">/</span><a class="login" href="#">LOGIN</a>
    </nav>
  </header>

  <section class="hero">
    <div class="hero-city" role="img" aria-label="Hazy aerial view of a city skyline with tall towers under a pale sky"></div>
    <h1 class="hero-title">Praesent elit nunc, aliquam vel diam</h1>
    <div class="device" role="img" aria-label="White smartphone showing a road map on its screen"></div>
    <div class="search-band">
      <p class="search-prompt">Who would you<br>like to find?</p>
      <div class="search-input">Find! Wab...</div>
      <div class="search-button">Look Up</div>
    </div>
  </section>

  <div class="feedback-tab"><span>FEEDBACK</span></div>

  <footer class="site-footer">
    <nav class="footer-links">
      <a href="#">About</a><span class="sep">|</span>
      <a href="#">Help</a><span class="sep">|</span>
      <a href="#">Contact</a><span class="sep">|</span>
      <a href="#">Privacy</a><span class="sep">|</span>
      <a href="#">Terms</a><span class="sep">|</span>
      <a href="#">Refunds</a><span class="sep">|</span>
      <a href="#">Faq</a>
    </nav>
    <p class="copyright">Copyright © 2014 Wablor. All rights reserved</p>
    <div class="social">
      <span class="social-dot one" role="img" aria-label="Social network one"></span>
      <span class="social-dot two" role="img" aria-label="Social network two"></span>
    </div>
    <p class="download-label">Download our application here :</p>
    <a class="store market" href="#"><span class="store-icon"></span><span class="store-text">Download it from<strong>APP MARKET</strong></span></a>
    <a class="store shelf" href="#"><span class="store-icon"></span><span class="store-text">Download it from<strong>PLAY SHELF</strong></span></a>
  </footer>
</body>
</html>
```